Vitamin/Dietary Supplement Company needs a simple Hemp CBD Health retail website to display a few...

We need a simple website designed that will allow us to display a few products for purchase. We are a vitamin/dietary supplement company that wants to set up a separate website for CBD health products. CBD is a chemical compound found in hemp and cannabis plants that provide various health and medicinal benefits. Our target audience are individuals that suffer from health issues and would like to treat their pain relief with CBD as an alternative to prescription medication and over the counter drugs such as Paxorin and Lumex. Looking for a simple and clean website that is easy for customers to navigate and purchase products.

Target Market(s)

Our target audience are individuals that suffer from health issues and would like to treat their pain relief with CBD as an alternative to prescription medication and over the counter drugs such as Paxorin and Lumex.

Coding

Coded - Design and coding required

Font styles to use
Serif

Colors

Designer to choose colors to be used in the design.

Requirements
Nice to have
• Homepage, About page, FAQ page, Contact page, Blog page

```html
<!DOCTYPE html>
<html lang="en">
<head>
<meta charset="utf-8">
<title>Hemvia – Home</title>
<link href="https://fonts.googleapis.com/css2?family=Open+Sans:wght@400;600;700&display=swap" rel="stylesheet">
<style>
:root{
  --green:#9bcb6c;
  --green-dark:#86b957;
  --ink:#222;
  --text:#555;
  --muted:#888;
  --line:#e6e6e6;
  --panel:#f4f4f4;
  --dark:#2a2a2a;
  --darker:#1f1f1f;
  --star:#f1b51c;
  --hero-blue:#1c93e6;
  --hero-navy:#15306e;
  --red:#e24b3b;
}
*{box-sizing:border-box;margin:0;padding:0}
html,body{width:1200px;height:2597px;overflow:hidden}
body{position:relative;background:#fff;font-family:"Open Sans",Arial,sans-serif;color:var(--text);font-size:11px}
.abs{position:absolute}
a{color:inherit;text-decoration:none}

.topbar{left:0;top:0;width:1200px;height:31px;background:var(--darker);color:#ccc;font-size:9px}
.topbar span{position:absolute;top:10px}
.brand{left:47px;top:52px;font-size:28px;font-weight:700;color:var(--ink);letter-spacing:.5px;line-height:1}
.brand-dot{display:inline-block;width:14px;height:14px;border-radius:50%;background:var(--green);margin-right:9px;vertical-align:2px}
.search{left:234px;top:56px;width:372px;height:31px;border:1px solid var(--line);font-size:9px;color:#aaa;padding:9px 10px}
.search svg{position:absolute;right:9px;top:9px}
.header-links{top:62px;font-size:10px;color:#444}

.side-menu{left:47px;top:113px;width:168px;height:150px;background:var(--green)}
.side-menu a{display:block;height:30px;line-height:30px;padding-left:17px;color:#fff;font-size:10px;font-weight:700;border-bottom:1px solid rgba(255,255,255,.35)}
.side-menu a:last-child{border:0}

.ph{display:block}
.hero{left:234px;top:113px;width:919px;height:507px;background:
  radial-gradient(ellipse 260px 200px at 88% 25%,#e9f0e2 0%,rgba(233,240,226,0) 100%),
  radial-gradient(ellipse 200px 260px at 8% 30%,#a9c994 0%,rgba(169,201,148,0) 100%),
  radial-gradient(ellipse 160px 120px at 48% 82%,#f3e3da 0%,rgba(243,227,218,0) 100%),
  radial-gradient(ellipse 240px 200px at 95% 70%,#b5d39c 0%,rgba(181,211,156,0) 100%),
  linear-gradient(120deg,#d9e0dc 0%,#eceeec 50%,#dde5d6 100%)}
.hero-kicker{left:234px;width:919px;top:276px;text-align:center;color:#fff;font-size:19px;letter-spacing:.5px}
.hero-line{top:310px;left:468px;font-size:38px;font-weight:700;line-height:46px;letter-spacing:2px}
.hero-line .box{background:var(--hero-blue);color:var(--hero-navy);padding:0 28px}
.hero-line .light{color:#fff;padding-left:6px}
.hero-line2{top:356px;left:446px;font-size:38px;font-weight:700;line-height:46px;letter-spacing:2px;background:var(--hero-blue);color:var(--hero-navy);padding:0 6px}
.btn-dark{background:#222;color:#fff;font-size:10px;font-weight:700;text-align:center}
.dots{top:608px;left:682px}
.dots i{display:inline-block;width:10px;height:3px;background:#fff;margin-right:5px}
.dots i.on{background:#333}

.promo{top:639px;width:294px;height:206px;text-align:center;color:#fff}
.promo h3{font-weight:600;font-size:20px;line-height:24px;margin-top:58px}
.promo small{display:block;font-size:15px;margin-bottom:2px}
.promo b{display:block;font-size:11px;margin-top:14px}

.h-sec{font-size:13px;font-weight:700;color:var(--ink)}
.arrows{font-size:12px;color:#333;letter-spacing:8px}

.card{width:170px;text-align:center}
.card .img{height:213px;background:#f2f2f2;position:relative}
.card .name{margin-top:19px;font-size:9px;color:#666}
.card .price{margin-top:6px;font-size:16px;color:var(--ink);font-weight:600}
.stars{font-size:9px;color:var(--star);letter-spacing:1px}
.stars i{font-style:normal;color:#ccc}
.btn-cart{background:var(--green);color:#fff;font-size:8px;font-weight:700;height:21px;line-height:21px;padding:0 9px;display:inline-block}

.women{left:47px;top:303px;width:168px;height:289px;background:
  radial-gradient(ellipse 70px 110px at 70% 40%,#f1c9b1 0%,rgba(241,201,177,0) 100%),
  radial-gradient(ellipse 60px 60px at 25% 85%,#3a2a2a 0%,rgba(58,42,42,0) 100%),
  linear-gradient(160deg,#f6dccd,#e3a98d)}
.women-txt{left:66px;top:338px;color:#fff;font-size:13px;line-height:18px;font-weight:600}
.women-txt b{font-size:30px;display:block;line-height:36px}

.news{left:47px;top:1046px;width:168px;height:280px;background:#262626;color:#bbb;text-align:center}
.news h4{color:#fff;font-size:12px;margin-top:40px}
.news p{font-size:8.5px;line-height:15px;margin:14px 14px 0}
.news .field{margin:22px 18px 0;height:26px;border:1px solid #444;background:#333;font-size:8px;color:#888;text-align:left;padding:7px 6px}
.news .sub{margin:10px 18px 0;height:26px;border:1px solid #666;color:#fff;font-size:8px;font-weight:700;line-height:24px}
.news .note{margin-top:26px}

.blog-img{left:47px;top:1399px;width:168px;height:118px;background:
  radial-gradient(ellipse 40px 55px at 40% 55%,#f0d8cc 0%,rgba(240,216,204,0) 100%),
  linear-gradient(135deg,#f1e2e0,#c99f9f)}
.blog-title{left:47px;top:1540px;width:168px;font-size:11px;font-weight:600;color:var(--ink);line-height:17px}
.blog-text{left:47px;top:1586px;width:168px;font-size:9px;line-height:14px;color:var(--muted)}
.blog-date{left:47px;top:1666px;font-size:8px;color:var(--red);font-weight:700}

.panel{left:234px;top:1235px;width:919px;height:284px;background:var(--panel)}
.about h4,.testi h4{font-size:13px;font-weight:700;color:var(--ink)}
.about h5{font-size:12px;font-weight:700;color:var(--ink);margin-top:20px}
.about .lead{font-size:11.5px;color:#333;line-height:20px;margin-top:12px;font-weight:600}
.about .body{font-size:9px;color:var(--muted);line-height:15px;margin-top:10px}
.testi .quote{font-size:10px;color:#555;line-height:17px;font-style:italic;margin-top:14px}
.avatar{width:52px;height:52px;border-radius:50%;background:radial-gradient(circle at 50% 40%,#9b8a7a,#3b3430)}

.summer{left:234px;top:1558px;width:294px;height:364px;background:
  radial-gradient(ellipse 110px 170px at 72% 40%,#f0d2bf 0%,rgba(240,210,191,0) 100%),
  radial-gradient(ellipse 140px 60px at 60% 95%,#fbfaf7 0%,rgba(251,250,247,0) 100%),
  linear-gradient(90deg,#f2f0ed 0%,#e6d2c3 100%)}
.summer-txt{left:258px;top:1630px;color:#444;font-size:14px;line-height:19px;font-weight:600}
.summer-txt .pct{font-size:60px;line-height:64px;color:var(--green);font-weight:600;display:block}
.summer-txt .off{font-size:28px;color:#555;margin-left:60px;display:block;line-height:28px}
.summer-txt .view{font-size:9px;color:var(--green);display:block;margin-top:18px}

.mini{width:290px;height:152px}
.mini .img{position:absolute;left:0;top:0;width:121px;height:152px;background:#f2f2f2}
.mini .info{position:absolute;left:140px;top:8px}
.mini .name{font-size:9px;color:#555}
.mini .price{font-size:15px;font-weight:600;color:var(--ink);margin-top:8px}
.mini .stars{margin-top:8px}
.mini .btn-cart{margin-top:10px}

.feat{width:280px;text-align:center}
.feat h6{font-size:10px;font-weight:700;color:var(--ink);margin-top:12px}
.feat .sub{font-size:9px;color:#999;margin-top:4px}
.feat p{font-size:9px;color:var(--muted);line-height:14px;margin-top:14px}

.footer{left:0;top:2140px;width:1200px;height:457px;background:var(--dark);color:#aaa}
.serv{top:2188px;font-size:10px;color:#fff;font-weight:700}
.serv small{display:block;font-weight:400;color:#aaa;font-size:8.5px;margin-top:3px}
.serv svg{position:absolute;left:-37px;top:-2px}
.f-rule{left:47px;width:1106px;height:1px;background:#3d3d3d}
.f-brand{left:47px;top:2288px;font-size:26px;font-weight:700;color:#fff;line-height:1}
.f-about{left:47px;top:2343px;width:220px;font-size:9px;line-height:14px;color:#bbb}
.f-about b{color:#fff;display:block;margin-top:8px}
.f-col{top:2302px;width:220px}
.f-col h6{font-size:10px;color:#fff;font-weight:700;margin-bottom:12px}
.f-col a{display:block;font-size:9px;line-height:23px;color:#aaa}
.f-col a:before{content:"›";margin-right:6px}
.social{left:47px;top:2443px}
.social i{display:inline-block;width:10px;height:10px;border-radius:50%;background:#888;margin-right:14px}
.pay{top:2560px;font-size:11px;font-weight:700;color:#9a9a9a}
</style>
</head>
<body>

<div class="abs topbar">
  <span style="left:47px">✈&nbsp; Free Shipping on Orders $50+</span>
  <span style="left:208px">☎&nbsp; Call us now: +0100 555 210</span>
  <span style="left:874px">My Account ▾</span>
  <span style="left:960px">Currency: USD ▾</span>
  <span style="left:1050px">Language: Germany ▾</span>
</div>

<div class="abs brand"><span class="brand-dot"></span>Hemvia</div>
<div class="abs search">Search entire store here...
  <svg width="12" height="12" viewBox="0 0 12 12"><circle cx="5" cy="5" r="4" fill="none" stroke="#666" stroke-width="1.4"/><path d="M8 8l3 3" stroke="#666" stroke-width="1.4"/></svg>
</div>
<div class="abs header-links" style="left:895px">
  <svg width="14" height="12" viewBox="0 0 14 12" style="vertical-align:middle"><rect x="0" y="6" width="3" height="6" fill="#333"/><rect x="5" y="2" width="3" height="10" fill="#333"/><rect x="10" y="5" width="3" height="7" fill="#333"/></svg>&nbsp; Compare
</div>
<div class="abs header-links" style="left:995px">
  <svg width="16" height="13" viewBox="0 0 16 13" style="vertical-align:middle"><path d="M8 12L2 6.5A3.3 3.3 0 0 1 8 2.5a3.3 3.3 0 0 1 6 4z" fill="none" stroke="#333" stroke-width="1.3"/></svg>&nbsp; Whishlist
</div>
<div class="abs" style="left:1094px;top:58px">
  <svg width="18" height="18" viewBox="0 0 18 18"><path d="M3 6h12l-1 10H4z" fill="none" stroke="#333" stroke-width="1.5"/><path d="M6 6V4a3 3 0 0 1 6 0v2" fill="none" stroke="#333" stroke-width="1.5"/></svg>
</div>

<nav class="abs side-menu">
  <a href="#">Shop <span style="float:right;margin-right:12px">›</span></a>
  <a href="#">Blog</a>
  <a href="#">Contact Us</a>
  <a href="#">About Us</a>
  <a href="#">Privacy Policy</a>
</nav>

<div class="abs hero ph" role="img" aria-label="Hand holding a jar of cream among white flowers and green leaves"></div>
<div class="abs hero-kicker">TOP WELLNESS TRENDS 2017</div>
<div class="abs hero-line"><span class="box">EXTRA</span><span class="light">NOURISH</span></div>
<div class="abs hero-line2">DIETARY SUPPLEMENTS</div>
<div class="abs btn-dark" style="left:648px;top:422px;width:84px;height:30px;line-height:30px">SHOP NOW</div>
<div class="abs dots"><i></i><i class="on"></i></div>

<div class="abs women ph" role="img" aria-label="Woman applying makeup with a brush"></div>
<div class="abs women-txt">WOMEN'S DAY<br>SALE OFF<b>30%</b></div>

<div class="abs promo ph" role="img" aria-label="Coconut oil in a glass bowl with mascara and leaves" style="left:234px;background:radial-gradient(ellipse 70px 60px at 55% 65%,#e8c94a 0%,rgba(232,201,74,0) 100%),radial-gradient(ellipse 90px 110px at 20% 60%,#a6c98a 0%,rgba(166,201,138,0) 100%),linear-gradient(135deg,#e3ecd9,#c9dbb9)">
  <h3><small>ORGANIC COCONUT OIL</small>GREEN COLLECTION</h3><b>BUY NOW!</b>
</div>
<div class="abs promo" style="left:547px;background:#c6d5ee">
  <h3>BUY 2 ITEMS<br>GET ONE FOR FREE</h3><b>BUY NOW!</b>
</div>
<div class="abs promo ph" role="img" aria-label="Halved avocado beside a dish of cream" style="left:859px;background:radial-gradient(ellipse 110px 70px at 50% 78%,#7b9a3a 0%,rgba(123,154,58,0) 100%),radial-gradient(ellipse 70px 45px at 70% 18%,#f4efe6 0%,rgba(244,239,230,0) 100%),linear-gradient(135deg,#d7e6e0,#b9d1c6)">
  <h3>CREAM AND<br>SLICES OF AVOCADO</h3><b>BUY NOW!</b>
</div>

<div class="abs h-sec" style="left:47px;top:622px">SPECIAL PRODUCTS</div>
<div class="abs arrows" style="left:188px;top:620px">‹ ›</div>
<div class="abs card" style="left:47px;top:658px;width:168px">
  <div class="img ph" role="img" aria-label="Green upholstered chair" style="height:208px;background:radial-gradient(ellipse 50px 70px at 50% 45%,#8aa05a 0%,rgba(138,160,90,0) 100%),#f2f2f2"></div>
  <div class="name" style="margin-top:20px">BRUKEN PIPE MODEL ENS</div>
  <div class="price">$15.79</div>
  <div class="stars">★★★★<i>★</i></div>
  <div style="margin-top:12px"><span class="btn-cart">🔒 ADD TO CART</span></div>
  <div style="margin-top:10px;font-size:10px;color:#333;letter-spacing:14px">♡▮◉</div>
</div>

<div class="abs h-sec" style="left:234px;top:880px">FEATURED PRODUCTS</div>
<div class="abs arrows" style="left:1123px;top:878px">‹ ›</div>
<div class="abs card" style="left:235px;top:916px"><div class="img ph" role="img" aria-label="Woman in a black jacket and dress" style="background:radial-gradient(ellipse 45px 95px at 50% 55%,#3b3630 0%,rgba(59,54,48,0) 100%),radial-gradient(ellipse 25px 30px at 50% 14%,#e6cf96 0%,rgba(230,207,150,0) 100%),#f2f2f2"></div><div class="name">BRUKEN PIPE MODEL EN2</div><div class="price">$15.76</div><div class="stars">★★★<i>★★</i></div></div>
<div class="abs card" style="left:419px;top:916px"><div class="img ph" role="img" aria-label="Pump bottle of oil with green leaves" style="background:radial-gradient(ellipse 25px 55px at 55% 48%,#b9c46a 0%,rgba(185,196,106,0) 100%),radial-gradient(ellipse 60px 25px at 45% 75%,#4f8a3a 0%,rgba(79,138,58,0) 100%),#f2f2f2"></div><div class="name">BRUKEN PIPE MODEL EN3</div><div class="price">$15.76</div><div class="stars">★★★<i>★★</i></div></div>
<div class="abs card" style="left:604px;top:916px"><div class="img ph" role="img" aria-label="Black vape pen" style="background:radial-gradient(ellipse 10px 80px at 50% 50%,#222 0%,rgba(34,34,34,0) 100%),#f2f2f2"></div><div class="name">BRUKEN PIPE MODEL EN4</div><div class="price">$15.76</div><div class="stars">★★★<i>★★</i></div></div>
<div class="abs card" style="left:788px;top:916px"><div class="img ph" role="img" aria-label="Orange lounge chair" style="background:radial-gradient(ellipse 55px 55px at 50% 50%,#e0773a 0%,rgba(224,119,58,0) 100%),#f2f2f2"></div><div class="name">BRUKEN PIPE MODEL ENA</div><div class="price">$15.76</div><div class="stars">★★★<i>★★</i></div></div>
<div class="abs card" style="left:973px;top:916px"><div class="img ph" role="img" aria-label="Green upholstered chair" style="background:radial-gradient(ellipse 50px 70px at 50% 45%,#8aa05a 0%,rgba(138,160,90,0) 100%),#f2f2f2"></div><div class="name">BRUKEN PIPE MODEL ENS</div><div class="price">$15.79</div><div class="stars">★★★★<i>★</i></div></div>

<div class="abs news">
  <h4>NEWSLETTER</h4>
  <p>Get all the latest information<br>on Events, Sales and Offers</p>
  <div class="field">Enter please your e-mail</div>
  <div class="sub">SUBSCRIBE</div>
  <p class="note">*Don't worry, we won't spam<br>our customers mailboxes</p>
</div>

<div class="abs h-sec" style="left:47px;top:1362px">OUR BLOG</div>
<div class="abs arrows" style="left:186px;top:1360px">‹ ›</div>
<div class="abs blog-img ph" role="img" aria-label="Woman in glasses on a city street"></div>
<div class="abs blog-title">HOW TO ROCK A BOW NO MATTER WHAT YOUR AGE</div>
<div class="abs blog-text">I've always loved anything finished off with pretty bow details. We often associate bows as a juvenile trend...</div>
<div class="abs blog-date">11-MAY</div>

<div class="abs panel"></div>
<div class="abs about" style="left:266px;top:1272px;width:390px">
  <h4>ABOUT US</h4>
  <h5>A Few Words About Us</h5>
  <div class="lead">A better way to shop online for furniture, home descor and so much more!</div>
  <div class="body">Solvane is more than just an online furniture store. We hand pick and curate the best in quality and style for you and your home. Why spend days driving from store to store trying to find that perfect look or</div>
  <div class="btn-dark" style="margin-top:22px;width:98px;height:27px;line-height:27px;font-size:9px">LEARN MORE</div>
</div>
<div class="abs testi" style="left:703px;top:1272px;width:410px">
  <h4>TESTIMONIALS</h4>
  <div style="margin-top:20px;color:var(--green);font-size:22px;line-height:10px;font-weight:700">“</div>
  <div class="quote">These guys are by far the best, have the most fantastic customer support that I have come across to date, I highly recommend people to buy and support these guys, their work is outstanding and the highest quality! Everything you are looking for! Shall def</div>
  <div style="position:relative;margin-top:16px;height:56px">
    <div class="avatar abs ph" role="img" aria-label="Customer portrait" style="left:0;top:0"></div>
    <div class="abs" style="left:70px;top:10px;font-size:10px;color:var(--green);font-weight:600">Marla Quint</div>
    <div class="abs" style="left:70px;top:28px;font-size:9px;color:#999;font-style:italic">Designer</div>
  </div>
</div>
<div class="abs" style="left:1078px;top:1479px"><i style="display:inline-block;width:10px;height:3px;background:var(--green);margin-right:4px"></i><i style="display:inline-block;width:10px;height:3px;background:#999;margin-right:4px"></i><i style="display:inline-block;width:10px;height:3px;background:#333"></i></div>

<div class="abs summer ph" role="img" aria-label="Woman with a white face mask"></div>
<div class="abs summer-txt">SUMMER<br>COLLECTION<br><span style="font-size:22px;line-height:34px;display:block;margin-top:6px">SALE</span><span class="pct">75%</span><span class="off">OFF</span><span class="view">VIEW COLLECTION ›</span></div>

<div class="abs h-sec" style="left:547px;top:1557px">BESTSELLER</div>
<div class="abs arrows" style="left:813px;top:1555px">‹ ›</div>
<div class="abs mini" style="left:547px;top:1595px"><div class="img ph" role="img" aria-label="Woman in a pink hat and white sweater" style="background:radial-gradient(ellipse 30px 50px at 50% 65%,#fafafa 0%,rgba(250,250,250,0) 100%),radial-gradient(ellipse 25px 30px at 45% 30%,#d9589a 0%,rgba(217,88,154,0) 100%),linear-gradient(#ececec,#e2e2e2)"></div><div class="info"><div class="name">NEON 70W TC BOX MOD2</div><div class="price">$28.99</div><div class="stars">★★★<i>★★</i></div><span class="btn-cart">🔒 ADD TO CART</span></div></div>
<div class="abs mini" style="left:547px;top:1768px"><div class="img ph" role="img" aria-label="Orange lounge chair" style="background:radial-gradient(ellipse 40px 40px at 50% 55%,#e0773a 0%,rgba(224,119,58,0) 100%),#f2f2f2"></div><div class="info"><div class="name">BRUKEN PIPE MODEL ENA</div><div class="price">$15.76</div><div class="stars">★★★<i>★★</i></div><span class="btn-cart">🔒 ADD TO CART</span></div></div>

<div class="abs h-sec" style="left:859px;top:1557px">NEW ARRIVALS</div>
<div class="abs arrows" style="left:1125px;top:1555px">‹ ›</div>
<div class="abs mini" style="left:859px;top:1595px"><div class="img ph" role="img" aria-label="Jar of cream with its box" style="background:radial-gradient(ellipse 30px 35px at 30% 50%,#f08a3a 0%,rgba(240,138,58,0) 100%),radial-gradient(ellipse 35px 25px at 65% 60%,#4a2a22 0%,rgba(74,42,34,0) 100%),#f2f2f2"></div><div class="info"><div class="name">NEON 70W TC BOX3</div><div class="price">$28.99</div><div class="stars">★★★<i>★★</i></div><span class="btn-cart">🔒 ADD TO CART</span></div></div>
<div class="abs mini" style="left:859px;top:1768px"><div class="img ph" role="img" aria-label="Tube of lotion with dried fruit" style="background:radial-gradient(ellipse 15px 45px at 55% 40%,#ffffff 0%,rgba(255,255,255,0) 100%),radial-gradient(ellipse 45px 20px at 45% 78%,#d86a2c 0%,rgba(216,106,44,0) 100%),#f2f2f2"></div><div class="info"><div class="name">BRUKEN PIPE MODEL ENS3</div><div class="price">$15.79</div><div class="stars">★★★<i>★★</i></div><span class="btn-cart">🔒 ADD TO CART</span></div></div>

<div class="abs feat" style="left:250px;top:1966px">
  <svg width="24" height="24" viewBox="0 0 24 24"><circle cx="12" cy="12" r="9" fill="none" stroke="var(--green)" stroke-width="3"/><circle cx="12" cy="12" r="4" fill="none" stroke="var(--green)" stroke-width="2"/></svg>
  <h6>CUSTOMER SUPPORT</h6><div class="sub">You Won't Be Alone</div>
  <p>We really care about you and your website as much as you do. Purchasing Solvane or any other theme from us you get 100% free support.</p>
</div>
<div class="abs feat" style="left:553px;top:1966px">
  <svg width="24" height="24" viewBox="0 0 24 24"><circle cx="12" cy="12" r="7" fill="none" stroke="var(--green)" stroke-width="4" stroke-dasharray="3 2"/><circle cx="12" cy="12" r="3" fill="var(--green)"/></svg>
  <h6>FULLY CUSTOMIZABLE</h6><div class="sub">Tons Of Options</div>
  <p>With Solvane you can customize the layout, colors and styles within only a few minutes. Start creating an amazing website right now!</p>
</div>
<div class="abs feat" style="left:859px;top:1966px">
  <svg width="24" height="24" viewBox="0 0 24 24"><path d="M3 6h18M3 12h18M3 18h18" stroke="var(--green)" stroke-width="2"/><rect x="6" y="3" width="3" height="6" fill="var(--green)"/><rect x="14" y="9" width="3" height="6" fill="var(--green)"/><rect x="8" y="15" width="3" height="6" fill="var(--green)"/></svg>
  <h6>POWERFUL ADMIN</h6><div class="sub">Made To Help You</div>
  <p>Solvane has very powerful admin features to help customer to build their own shop in minutes without any special skills in web development.</p>
</div>

<div class="abs footer"></div>
<div class="abs serv" style="left:117px">
  <svg width="26" height="24" viewBox="0 0 26 24"><path d="M2 11L24 2 17 22 12 14z" fill="none" stroke="var(--green)" stroke-width="2"/></svg>
  FREE SHIPPING &amp; DELIVERY<small>Free on all products</small></div>
<div class="abs serv" style="left:373px">
  <svg width="22" height="22" viewBox="0 0 22 22"><path d="M4 2l4 4-2 3c1.5 3 4 5.5 7 7l3-2 4 4-3 3C9 21 1 13 1 5z" fill="var(--green)"/></svg>
  +0100 555 210 : +0100 555 210<small>Free support line!</small></div>
<div class="abs serv" style="left:642px">
  <svg width="26" height="20" viewBox="0 0 26 20"><rect x="1" y="1" width="24" height="18" fill="var(--green)"/><path d="M1 1l12 10L25 1" fill="none" stroke="var(--dark)" stroke-width="2"/></svg>
  SUPPORT@VERDANTHOUSE.COM<small>Orders Support!</small></div>
<div class="abs serv" style="left:906px">
  <svg width="24" height="24" viewBox="0 0 24 24"><circle cx="12" cy="12" r="10" fill="none" stroke="var(--green)" stroke-width="2.5"/><path d="M12 6v6l4 3" fill="none" stroke="var(--green)" stroke-width="2"/></svg>
  MON - FRI / 8:00 - 18:00<small>Working Days/Hours!</small></div>
<div class="abs f-rule" style="top:2256px"></div>

<div class="abs f-brand"><span class="brand-dot"></span>Hemvia</div>
<div class="abs f-about">We are a team of designers and developers that create high quality Shopcraft, Storelane, Cartwise.<b>Contact info:</b>42-B, Greenway Park, Harbor District</div>
<div class="abs social"><i></i><i></i><i></i><i></i><i></i><i></i></div>

<div class="abs f-col" style="left:329px"><h6>CUSTOMER SERVICE</h6><a>Contact Us</a><a>Returns</a><a>Order History</a><a>Site Map</a><a>Testimonials</a><a>My Account</a><a>Unsubscribe Notification</a></div>
<div class="abs f-col" style="left:610px"><h6>INFORMATION</h6><a>About Us</a><a>Delivery Information</a><a>Privacy Policy</a><a>Terms &amp; Conditions</a><a>Warranty</a><a>FAQ</a><a>Seller Login</a></div>
<div class="abs f-col" style="left:890px"><h6>EXTRAS</h6><a>Brands</a><a>Gift Vouchers</a><a>Affiliates</a><a>Wish List</a><a>Order History</a><a>Track Your Order</a></div>

<div class="abs f-rule" style="top:2530px"></div>
<div class="abs pay" style="left:862px">Paylo</div>
<div class="abs pay" style="left:929px">Findra</div>
<div class="abs pay" style="left:1005px">Cirqa</div>
<div class="abs pay" style="left:1060px">Duoro</div>
<div class="abs pay" style="left:1118px">Vesto</div>

</body>
</html>
```